Designing business cards for my start-up business

The company is called Pellion. We are a start-up tech data company based in Guernsey, Channel Islands. We want the business cards to look clean, fresh and innovative, just what a tech company should be. We do not want the business cards to look corporate or too official such as a bank. I would like the front of the business card to have our logo and the tag line of "Linking People". On the back will be our contact details, emails etc. However I am open to your ideas and suggestions. I have provided all our logos and a word doc of all our contact details. There are 4 directors of the business, so I want 4 versions of the same design.

Target Market(s)

Our clients are businesses of all industries. Its a broad target market.

Industry/Entity Type

Information Technology

Contact Information for Business Card

I have attached a word doc called "Business Cards info" which gives all contact details of the 4 employees for the company.

Requirements
Must have
• We must have our logo and the tag line of "Linking People". This could on the front of the card and then the individuals contact details on the back. Other than that, I'm happy for the designers to come up with ideas/styles.
Nice to have
• N/A
Should not have
• I don't want the cards to look too formal or corporate. As mentioned, we are a tech start-up so we want to look innovative.

```html
<!DOCTYPE html>
<html lang="en">
<head>
<meta charset="utf-8">
<title>Pellion business cards</title>
<link href="https://fonts.googleapis.com/css2?family=Open+Sans:wght@400;600;700&display=swap" rel="stylesheet">
<style>
  :root {
    --orange: #f65a36;
    --ink: #2b2b2b;
    --ink-soft: #555555;
    --rule: #d9d9d9;
    --paper: #ffffff;
    --backdrop: #ecebe8;
  }
  * { margin: 0; padding: 0; box-sizing: border-box; }
  html, body {
    width: 1200px; height: 950px; overflow: hidden;
    background: var(--backdrop);
    font-family: "Open Sans", sans-serif;
  }
  .sheet {
    width: 1200px; height: 950px;
    display: flex; flex-direction: column; align-items: center; justify-content: center;
    gap: 50px;
  }
  .card {
    width: 700px; height: 400px;
    position: relative; overflow: hidden;
    box-shadow: 0 6px 18px rgba(0,0,0,.18);
  }

  /* Contact side */
  .card--contact { background: var(--paper); }
  .brand-block {
    position: absolute; left: 60px; top: 120px; width: 220px;
    display: flex; flex-direction: column; align-items: flex-start; gap: 18px;
  }
  .brand-mark { display: block; width: 110px; height: 110px; background: var(--orange); }
  .brand-name {
    font-size: 30px; font-weight: 600; color: var(--ink);
    letter-spacing: 8px; line-height: 1;
  }
  .details {
    position: absolute; left: 330px; top: 70px; width: 330px;
  }
  .person-name { font-size: 28px; font-weight: 600; color: var(--orange); line-height: 1.1; }
  .person-role { font-size: 17px; color: var(--ink); margin-top: 2px; }
  .details-rule { height: 1px; background: var(--rule); margin: 14px 0; }
  .address { font-size: 15px; color: var(--ink-soft); line-height: 1.5; }
  .contact-line {
    display: flex; align-items: center; gap: 10px;
    font-size: 15px; color: var(--ink-soft); margin-top: 6px;
  }
  .contact-line--first { margin-top: 12px; }
  .contact-icon { width: 16px; height: 16px; flex: none; }
  .web-band {
    position: absolute; right: 0; bottom: 0;
    width: 400px; height: 48px;
    background: var(--orange);
    display: flex; align-items: center; justify-content: flex-end;
    padding-right: 30px;
  }
  .web-address { color: var(--paper); font-size: 15px; letter-spacing: 5px; }

  /* Brand side */
  .card--brand { background: var(--orange); }
  .brand-center {
    position: absolute; inset: 0;
    display: flex; flex-direction: column; align-items: center; justify-content: center;
    gap: 20px;
  }
  .brand-lockup { display: flex; align-items: center; gap: 18px; }
  .brand-lockup .brand-mark { width: 44px; height: 44px; background: var(--paper); }
  .brand-lockup .brand-name { color: var(--paper); font-size: 52px; letter-spacing: 6px; }
  .tagline { color: var(--paper); font-size: 20px; letter-spacing: 2px; }
</style>
</head>
<body>
<main class="sheet">

  <section class="card card--contact" aria-label="Contact side">
    <div class="brand-block">
      <span class="brand-mark"></span>
      <span class="brand-name">Pellion</span>
    </div>
    <div class="details">
      <p class="person-name">Luc Mahy</p>
      <p class="person-role">Director</p>
      <div class="details-rule"></div>
      <p class="address">12 Rue Marchant, St Sampson<br>Guernsey, GY2 4QA<br>Channel Islands</p>
      <p class="contact-line contact-line--first">
        <svg class="contact-icon" viewBox="0 0 16 16"><rect x="1.5" y="1.5" width="13" height="13" fill="none" stroke="var(--orange)" stroke-width="2"/></svg>
        +44 7700 900 214
      </p>
      <p class="contact-line">
        <svg class="contact-icon" viewBox="0 0 16 16"><rect x="0" y="0" width="16" height="16" fill="var(--orange)"/><path d="M3.5 8 L7 11.5 L12.5 4.5" fill="none" stroke="#fff" stroke-width="1.8"/></svg>
        LucMahy@pellion.gg
      </p>
    </div>
    <div class="web-band"><span class="web-address">www.pellion.gg</span></div>
  </section>

  <section class="card card--brand" aria-label="Brand side">
    <div class="brand-center">
      <div class="brand-lockup">
        <span class="brand-mark"></span>
        <span class="brand-name">Pellion</span>
      </div>
      <p class="tagline">Linking People</p>
    </div>
  </section>

</main>
</body>
</html>
```